Scheduled Servicing Forms

Corvella Systems requires two schedule servicing forms to be created on designer templates for our engineers to complete when servicing customers. We will complete these forms on a periodic basis, and send to the customer on completion of the work.
We have two forms that need to be created:
• Hybrid Cloud Customer Service
• Veltrix Cloud Customer Service
Please do not reference our website for ideas as its about to change. “Specialised Consulting” is our new go to market, not “Pushing the Boundaries of Technology. Our new website (still under development) is available at https://corvellasystems.qzt.net.au and will be officially launched shortly.
Our company theme is “Blue” and we want to keep a blue theme for the work.
Please ensure there is “Ample” space for engineers to write comments next to each audit item.
We have uploaded examples of the content that needs to be created for both form in Word and Excel format.
The designer must upload the source files (not just PDF) so we can edit the content on the forms at a later date.
The forms must be in standard A4 size (multiple pages).
Industry/Entity Type
Information Technology
Look and feel

```html
<!DOCTYPE html>
<html lang="en">
<head>
<meta charset="utf-8">
<title>Corvella Systems – Veltrix Cloud Customer Scheduled Service Checklist</title>
<link href="https://fonts.googleapis.com/css2?family=Arimo:wght@400;700&display=swap" rel="stylesheet">
<style>
  :root {
    --brand-blue: #23519e;
    --brand-blue-deep: #1d4690;
    --sky-light: #dde6f1;
    --sky-mid: #c9d8ea;
    --row-light: #eef2f7;
    --row-shade: #d3dfec;
    --ink: #1d2433;
    --line: #3b5aa8;
    --box: #4c6fb8;
    --stage: #eceff3;
  }
  * { box-sizing: border-box; margin: 0; padding: 0; }
  html, body { width: 1200px; height: 1200px; overflow: hidden; }
  body {
    background: var(--stage);
    font-family: "Arimo", Arial, sans-serif;
    color: var(--ink);
    position: relative;
  }
  .form-page {
    position: absolute;
    left: 211px; top: 50px;
    width: 778px; height: 1100px;
    background: linear-gradient(160deg, #e4ebf4 0%, var(--sky-light) 45%, #d5e0ee 100%);
    overflow: hidden;
    box-shadow: 0 6px 24px rgba(0,0,0,.15);
  }
  .page-art { position: absolute; inset: 0; width: 100%; height: 100%; }
  .circuit-texture {
    position: absolute; right: 0; top: 40px; width: 520px; height: 330px;
    background: radial-gradient(ellipse at 70% 40%, rgba(255,255,255,.55), rgba(255,255,255,0) 70%);
  }
  .brand {
    position: absolute; left: 40px; top: 78px;
    display: flex; align-items: center; gap: 12px;
  }
  .brand-mark { width: 30px; height: 30px; background: var(--brand-blue); }
  .brand-name {
    font-size: 26px; font-weight: 700; color: var(--brand-blue);
    letter-spacing: .5px;
  }
  .form-title {
    position: absolute; left: 40px; top: 130px;
    font-size: 15px; line-height: 18px; color: var(--ink);
    border-top: 1.5px solid var(--brand-blue); padding-top: 6px; width: 300px;
  }
  .meta { position: absolute; left: 40px; top: 190px; width: 690px; }
  .meta-row { display: flex; align-items: flex-end; height: 36px; font-size: 19px; }
  .meta-row .label { width: 110px; }
  .meta-row .fill { flex: 1; border-bottom: 1px solid var(--ink); height: 22px; }
  .meta-row .date-fill { width: 260px; display: flex; justify-content: space-around;
    border-bottom: 1px solid var(--ink); font-size: 15px; height: 22px; }
  .checklist {
    position: absolute; left: 40px; top: 290px; width: 690px;
    border-collapse: collapse;
  }
  .checklist th {
    background: var(--brand-blue); color: #fff; font-weight: 400;
    font-size: 19px; text-align: left; padding: 6px 10px; height: 34px;
  }
  .checklist td { height: 56px; vertical-align: middle; font-size: 14px; line-height: 16px; }
  .checklist .item { width: 300px; padding: 4px 12px; }
  .checklist tr:nth-child(odd) td { background: var(--row-light); }
  .checklist tr:nth-child(even) td { background: var(--row-shade); }
  .checklist tr.is-highlight td { background: var(--brand-blue); color: #fff; }
  .checklist tr.is-highlight .tick-box { border-color: #fff; background: #fff; }
  .checklist tr.is-highlight .comment-line { border-color: #fff; }
  .result { padding: 4px 14px; font-size: 13px; }
  .answer { display: flex; align-items: center; gap: 6px; height: 20px; }
  .answer .no { margin-left: 70px; display: flex; align-items: center; gap: 6px; }
  .tick-box { width: 14px; height: 14px; border: 1.5px solid var(--box); background: #fff; }
  .comment { display: flex; align-items: flex-end; gap: 8px; height: 22px; }
  .comment-line { flex: 1; border-bottom: 1.5px solid var(--line); height: 14px; }
</style>
</head>
<body>
  <main class="form-page">
    <svg class="page-art" viewBox="0 0 778 1100" preserveAspectRatio="none" aria-hidden="true">
      <polygon points="0,0 778,0 778,60 470,40 0,70" fill="var(--brand-blue)"/>
      <polygon points="0,70 470,40 778,60 778,72 470,54 0,82" fill="#ffffff" opacity=".8"/>
      <polygon points="778,880 420,1100 778,1100" fill="var(--brand-blue-deep)"/>
      <polygon points="0,960 0,1100 420,1100" fill="var(--brand-blue)"/>
      <polygon points="778,760 520,1030 778,880" fill="#7ea3cf" opacity=".8"/>
      <polygon points="560,900 640,1060 700,820" fill="#ffffff" opacity=".35"/>
    </svg>
    <div class="circuit-texture" role="img" aria-label="Faint circuit-board line pattern"></div>

    <div class="brand">
      <span class="brand-mark"></span>
      <span class="brand-name">CORVELLA SYSTEMS</span>
    </div>
    <p class="form-title">Veltrix Cloud Customer<br>Scheduled Service Checklist</p>

    <div class="meta">
      <div class="meta-row"><span class="label">Customer</span><span class="fill"></span></div>
      <div class="meta-row"><span class="label">Date</span><span class="date-fill"><span>/</span><span>/</span></span></div>
    </div>

    <table class="checklist">
      <thead><tr><th>Maintenance Check</th><th>Result</th></tr></thead>
      <tbody>
        <tr><td class="item">Active Bckup for all Veltrix 365 accounts (manual check) -ensuring all items are included in the job</td><td class="result"><div class="answer">Yes <span class="tick-box"></span><span class="no">No <span class="tick-box"></span></span></div><div class="comment">Comment <span class="comment-line"></span></div></td></tr>
        <tr><td class="item">Test restore of an email</td><td class="result"><div class="answer">Yes <span class="tick-box"></span><span class="no">No <span class="tick-box"></span></span></div><div class="comment">Comment <span class="comment-line"></span></div></td></tr>
        <tr><td class="item">Test restore of ShareVault file</td><td class="result"><div class="answer">Yes <span class="tick-box"></span><span class="no">No <span class="tick-box"></span></span></div><div class="comment">Comment <span class="comment-line"></span></div></td></tr>
        <tr class="is-highlight"><td class="item">Log into antivirus products(ensure aall endpoint desices have active antivirus and are up to date)</td><td class="result"><div class="answer">Yes <span class="tick-box"></span><span class="no">No <span class="tick-box"></span></span></div><div class="comment">Comment <span class="comment-line"></span></div></td></tr>
        <tr><td class="item">Check Spam filtes</td><td class="result"><div class="answer">Yes <span class="tick-box"></span><span class="no">No <span class="tick-box"></span></span></div><div class="comment">Comment <span class="comment-line"></span></div></td></tr>
        <tr><td class="item">Check that all users have MFA enabled</td><td class="result"><div class="answer">Yes <span class="tick-box"></span><span class="no">No <span class="tick-box"></span></span></div><div class="comment">Comment <span class="comment-line"></span></div></td></tr>
        <tr><td class="item">Review Veltrix 365 Risk Detections (user and Device Logins)</td><td class="result"><div class="answer">Yes <span class="tick-box"></span><span class="no">No <span class="tick-box"></span></span></div><div class="comment">Comment <span class="comment-line"></span></div></td></tr>
        <tr><td class="item">Confirm Audit Logging enabled</td><td class="result"><div class="answer">Yes <span class="tick-box"></span><span class="no">No <span class="tick-box"></span></span></div><div class="comment">Comment <span class="comment-line"></span></div></td></tr>
        <tr><td class="item">Review external sharing in ShareVault/DriveNest</td><td class="result"><div class="answer">Yes <span class="tick-box"></span><span class="no">No <span class="tick-box"></span></span></div><div class="comment">Comment <span class="comment-line"></span></div></td></tr>
        <tr><td class="item">Check Compliance status</td><td class="result"><div class="answer">Yes <span class="tick-box"></span><span class="no">No <span class="tick-box"></span></span></div><div class="comment">Comment <span class="comment-line"></span></div></td></tr>
        <tr><td class="item">Check and record Veltrix security score</td><td class="result"><div class="answer">Yes <span class="tick-box"></span><span class="no">No <span class="tick-box"></span></span></div><div class="comment">Comment <span class="comment-line"></span></div></td></tr>
      </tbody>
    </table>
  </main>
</body>
</html>
```